UI/UX: Design Digital Business Card Layout

Hello,

I need to design a small web page layout ..
It is a small web page for mobile contains icons with links + logo (Phone icon, email icon, plazmoro icon .. etc).
Dimensions: 1080x1920px (Portrait).

PLEASE SEE THE ATTACHED EXAMPLES.
THIS IS NOT A PAPER REGULAR BUSINESS CARD.

I need a beautiful and creative layouts including:
User interface
Icons design.
CATCHY DESIGN.

```html
<!DOCTYPE html>
<html lang="en">
<head>
<meta charset="UTF-8">
<title>Digital Business Card</title>
<link href="https://fonts.googleapis.com/css2?family=Carlito:wght@400;700&display=swap" rel="stylesheet">
<style>
  :root {
    --coral: #f0474f;
    --pink: #ff3366;
    --orange: #ff6a00;
    --ring: #ff3d6e;
    --rule: #f59a9a;
    --white: #ffffff;
    --avatar-soft: #ffd9d6;
  }
  * { margin: 0; padding: 0; box-sizing: border-box; }
  html, body { width: 675px; height: 1200px; overflow: hidden; background: var(--white); }
  body { font-family: "Carlito", "Calibri", sans-serif; color: var(--coral); }
  .card { position: relative; width: 675px; height: 1200px; background: var(--white); overflow: hidden; }

  .header-band {
    position: absolute; left: 0; top: 0; width: 675px; height: 304px;
    background: linear-gradient(135deg, var(--pink) 0%, var(--orange) 100%);
  }
  .brand-logo {
    position: absolute; left: 0; top: 47px; width: 100%; text-align: center;
    font-size: 57px; font-weight: 700; color: var(--white); letter-spacing: 1px; line-height: 1;
  }

  .avatar {
    position: absolute; left: 225px; top: 167.5px; width: 225px; height: 225px;
    border-radius: 50%; border: 5px solid var(--ring); background: var(--white); overflow: hidden;
  }
  .avatar-fill {
    width: 100%; height: 100%;
    background: radial-gradient(circle at 50% 40%, var(--avatar-soft) 0%, #ffb3ad 100%);
  }

  .person-name {
    position: absolute; left: 0; top: 418px; width: 100%; text-align: center;
    font-size: 42px; font-weight: 400; letter-spacing: 0.5px; line-height: 1;
  }
  .person-role {
    position: absolute; left: 0; top: 469px; width: 100%; text-align: center;
    font-size: 29px; font-weight: 400; letter-spacing: 0.5px; line-height: 1;
  }

  .social-links {
    position: absolute; left: 0; top: 528px; width: 100%;
    display: flex; justify-content: center; gap: 4px; list-style: none;
  }
  .social-links li { width: 62px; display: flex; flex-direction: column; align-items: center; }
  .social-dot { width: 37px; height: 37px; border-radius: 50%; background: var(--coral); }
  .social-name { margin-top: 5px; font-size: 12px; font-weight: 700; line-height: 1; white-space: nowrap; }

  .divider { position: absolute; left: 37.5px; width: 600px; height: 2px; background: var(--rule); }
  .divider--top { top: 619px; }
  .divider--bottom { top: 950px; }

  .contact-list { position: absolute; left: 76px; top: 671px; list-style: none; }
  .contact-item { display: flex; align-items: center; height: 63px; margin-bottom: 20px; }
  .contact-icon { width: 63px; height: 63px; flex: none; }
  .contact-text { margin-left: 20px; font-size: 31px; font-weight: 700; line-height: 1; white-space: nowrap; }

  .location-pin { position: absolute; left: 315px; top: 975px; width: 45px; height: 65px; }
  .address {
    position: absolute; left: 0; top: 1059px; width: 100%; text-align: center;
    font-size: 21.5px; font-weight: 700; line-height: 28.3px; font-style: normal;
  }
</style>
</head>
<body>
<main class="card">
  <header class="header-band">
    <div class="brand-logo">LOGO</div>
  </header>

  <div class="avatar">
    <div class="avatar-fill" role="img" aria-label="Profile photo of the card owner"></div>
  </div>

  <h1 class="person-name">NAME PLEASE</h1>
  <p class="person-role">PROFESSION</p>

  <ul class="social-links">
    <li><span class="social-dot"></span><span class="social-name">Snapora</span></li>
    <li><span class="social-dot"></span><span class="social-name">plazmoro</span></li>
    <li><span class="social-dot"></span><span class="social-name">Chirply</span></li>
    <li><span class="social-dot"></span><span class="social-name">Searchwell</span></li>
    <li><span class="social-dot"></span><span class="social-name">Linkvera</span></li>
  </ul>

  <div class="divider divider--top"></div>

  <ul class="contact-list">
    <li class="contact-item">
      <svg class="contact-icon" viewBox="0 0 64 64" aria-hidden="true">
        <circle cx="32" cy="32" r="32" fill="var(--coral)"/>
        <path d="M22 16c2-1 4 0 5 2l3 6c1 2 0 3-1 4l-2 2c1 4 5 8 9 10l2-2c1-1 3-2 4-1l6 3c2 1 3 3 2 5l-2 4c-1 2-3 3-6 2-11-3-20-12-23-23-1-3 0-5 2-6z" fill="var(--white)"/>
      </svg>
      <span class="contact-text">+ x xxxxxxxxxx</span>
    </li>
    <li class="contact-item">
      <svg class="contact-icon" viewBox="0 0 64 64" aria-hidden="true">
        <circle cx="32" cy="32" r="32" fill="var(--coral)"/>
        <rect x="15" y="20" width="34" height="24" fill="none" stroke="var(--white)" stroke-width="2.5"/>
        <path d="M15 20l17 14 17-14" fill="none" stroke="var(--white)" stroke-width="2.5"/>
      </svg>
      <span class="contact-text">name.company@mailnest.com</span>
    </li>
    <li class="contact-item">
      <svg class="contact-icon" viewBox="0 0 64 64" aria-hidden="true">
        <circle cx="32" cy="32" r="32" fill="var(--coral)"/>
        <circle cx="32" cy="32" r="19" fill="none" stroke="var(--white)" stroke-width="2.5"/>
        <ellipse cx="32" cy="32" rx="8" ry="19" fill="none" stroke="var(--white)" stroke-width="2"/>
        <line x1="13" y1="32" x2="51" y2="32" stroke="var(--white)" stroke-width="2"/>
        <line x1="16" y1="23" x2="48" y2="23" stroke="var(--white)" stroke-width="1.6"/>
        <line x1="16" y1="41" x2="48" y2="41" stroke="var(--white)" stroke-width="1.6"/>
      </svg>
      <span class="contact-text">www.namevanta-studio.com</span>
    </li>
  </ul>

  <div class="divider divider--bottom"></div>

  <svg class="location-pin" viewBox="0 0 45 65" aria-hidden="true">
    <path d="M22.5 0C10 0 0 10 0 22.5 0 36 22.5 65 22.5 65S45 36 45 22.5C45 10 35 0 22.5 0z" fill="var(--coral)"/>
    <circle cx="22.5" cy="22" r="8.5" fill="var(--white)"/>
  </svg>

  <address class="address">
    NAME PLEASE<br>
    ADDRESS,STREET,DOOR NO<br>
    PIN: XXXXXX<br>
    COUNTRY
  </address>
</main>
</body>
</html>
```